Larder & Flame - Premium Catering needs a new menu design.

I currently use menupro to make my own menus for printing and uploading to the website (PDF). I need a professional menu to replace my current menu. I wold like to mail these menus out so I'm thinking a tri-fold menu would be the best option. Similar to what pizzerias send out.

Logo Text

Would be good to reduce the text thickness of the letters "MIL" in the word MILLRUN. Right now MIL has thicker text.

Colors

Designer to choose colors to be used in the design.

```html
<!DOCTYPE html>
<html lang="en">
<head>
<meta charset="utf-8">
<title>Millrun — Larder &amp; Flame Menu</title>
<link rel="stylesheet" href="https://fonts.googleapis.com/css2?family=Bebas+Neue&family=Open+Sans:wght@400;600;700&family=Lato:wght@400&display=swap">
<style>
  :root {
    --navy: #1b1e2b;
    --lime: #a6fc4a;
    --orange: #ee7800;
    --tan: #d9c793;
    --maroon: #6e0b0b;
    --white: #ffffff;
  }
  * { margin: 0; padding: 0; box-sizing: border-box; }
  html, body { width: 1200px; height: 1200px; overflow: hidden; background: var(--white); }
  .canvas { position: relative; width: 1200px; height: 1200px; }

  .panel { position: absolute; top: 140px; width: 483px; height: 859px; overflow: hidden; }
  .panel--cover { left: 79px; background: var(--lime); }
  .panel--list { left: 636px; background: var(--lime); }
  .panel__shapes { position: absolute; inset: 0; }

  .footer-band { position: absolute; left: 0; bottom: 0; width: 100%; height: 50px; background: var(--orange);
    display: flex; align-items: center; justify-content: center; }
  .footer-band__url { font-family: "Open Sans", sans-serif; font-weight: 700; font-size: 20px; color: var(--white); }

  .brand { position: absolute; left: 0; width: 100%; text-align: center; color: var(--maroon);
    font-family: "Open Sans", sans-serif; font-weight: 700; line-height: 1; }
  .brand__name, .brand__line { display: block; }

  .panel--cover .brand { top: 172px; }
  .panel--cover .brand__name { font-size: 50px; letter-spacing: 1px; }
  .panel--cover .brand__line--1 { font-size: 28px; margin-top: 12px; letter-spacing: 1px; }
  .panel--cover .brand__line--2 { font-size: 23px; margin-top: 8px; letter-spacing: 1px; }

  .panel--list .brand { top: 68px; }
  .panel--list .brand__name { font-size: 30px; }
  .panel--list .brand__line--1 { font-size: 16px; margin-top: 5px; }
  .panel--list .brand__line--2 { font-size: 13px; margin-top: 4px; letter-spacing: .5px; }

  .cover__title { position: absolute; top: 480px; left: 0; width: 100%; text-align: center;
    font-family: "Bebas Neue", sans-serif; font-size: 120px; line-height: 1; color: var(--navy); letter-spacing: 2px; }
  .cover__service { position: absolute; top: 593px; left: 0; width: 100%; text-align: center;
    font-family: "Open Sans", sans-serif; font-size: 21px; color: var(--orange); }
  .cover__delivery { position: absolute; top: 635px; left: 123px; width: 237px; height: 42px; background: var(--orange);
    display: flex; align-items: center; justify-content: center;
    font-family: "Bebas Neue", sans-serif; font-size: 28px; letter-spacing: 1.5px; color: var(--white); word-spacing: 6px; }
  .cover__contact { position: absolute; top: 686px; left: 0; width: 100%; text-align: center;
    font-family: "Open Sans", sans-serif; font-size: 17px; color: var(--orange); }
  .cover__phone { position: absolute; top: 709px; left: 0; width: 100%; text-align: center;
    font-family: "Open Sans", sans-serif; font-weight: 700; font-size: 20px; color: var(--navy); }

  .section-title { position: absolute; left: 0; width: 100%; text-align: center;
    font-family: "Bebas Neue", sans-serif; font-size: 28px; line-height: 1; color: var(--tan); letter-spacing: .5px; }

  .menu-item { position: absolute; left: 78px; width: 327px; }
  .menu-item__row { display: flex; align-items: baseline; font-family: "Open Sans", sans-serif; font-size: 16px;
    line-height: 20px; color: var(--orange); }
  .menu-item__leader { flex: 1; margin: 0 6px; border-bottom: 1px dashed var(--white); transform: translateY(-2px); }
  .menu-item__price { font-weight: 600; }
  .menu-item__desc { font-family: "Lato", sans-serif; font-size: 9.5px; line-height: 10.5px; color: var(--white); margin-top: 2px; }
</style>
</head>
<body>
<main class="canvas">

  <section class="panel panel--cover">
    <svg class="panel__shapes" width="483" height="859" viewBox="0 0 483 859">
      <path d="M0 0 H483 V304 Q241.5 540 0 304 Z" fill="var(--orange)"/>
      <path d="M0 0 H483 V235 Q241.5 535 0 235 Z" fill="var(--navy)"/>
    </svg>
    <div class="brand">
      <span class="brand__name">MILLRUN</span>
      <span class="brand__line brand__line--1">LARDER &amp; FLAME</span>
      <span class="brand__line brand__line--2">PREMIUM CATERING</span>
    </div>
    <h1 class="cover__title">MENU</h1>
    <p class="cover__service">DINE-IN / TAKE-OUT</p>
    <p class="cover__delivery">FOR FOOD DELIVERY</p>
    <p class="cover__contact">Just contact us for orders</p>
    <p class="cover__phone">555-014-2273</p>
    <div class="footer-band"><span class="footer-band__url">www.millrunkitchen.com</span></div>
  </section>

  <section class="panel panel--list">
    <svg class="panel__shapes" width="483" height="859" viewBox="0 0 483 859">
      <path d="M0 222 Q241.5 68 483 226 V859 H0 Z" fill="var(--navy)"/>
    </svg>
    <div class="brand">
      <span class="brand__name">MILLRUN</span>
      <span class="brand__line brand__line--1">LARDER &amp; FLAME</span>
      <span class="brand__line brand__line--2">PREMIUM CATERING</span>
    </div>

    <h2 class="section-title" style="top:168px">BREAKFAST</h2>
    <div class="menu-item" style="top:214px"><div class="menu-item__row"><span>Name of dish</span><span class="menu-item__leader"></span><span class="menu-item__price">$10</span></div><p class="menu-item__desc">Lorem ipsum dolor sit amet, consectetur<br>adipiscing elit, sed do eiusmod tempor</p></div>
    <div class="menu-item" style="top:265px"><div class="menu-item__row"><span>Name of dish</span><span class="menu-item__leader"></span><span class="menu-item__price">$10</span></div><p class="menu-item__desc">Lorem ipsum dolor sit amet, consectetur<br>adipiscing elit, sed do eiusmod tempor</p></div>
    <div class="menu-item" style="top:316px"><div class="menu-item__row"><span>Name of dish</span><span class="menu-item__leader"></span><span class="menu-item__price">$10</span></div><p class="menu-item__desc">Lorem ipsum dolor sit amet, consectetur<br>adipiscing elit, sed do eiusmod tempor</p></div>

    <h2 class="section-title" style="top:387px">PLATTERS</h2>
    <div class="menu-item" style="top:425px"><div class="menu-item__row"><span>Name of dish</span><span class="menu-item__leader"></span><span class="menu-item__price">$10</span></div><p class="menu-item__desc">Lorem ipsum dolor sit amet, consectetur<br>adipiscing elit, sed do eiusmod tempor</p></div>
    <div class="menu-item" style="top:475px"><div class="menu-item__row"><span>Name of dish</span><span class="menu-item__leader"></span><span class="menu-item__price">$10</span></div><p class="menu-item__desc">Lorem ipsum dolor sit amet, consectetur<br>adipiscing elit, sed do eiusmod tempor</p></div>
    <div class="menu-item" style="top:526px"><div class="menu-item__row"><span>Name of dish</span><span class="menu-item__leader"></span><span class="menu-item__price">$10</span></div><p class="menu-item__desc">Lorem ipsum dolor sit amet, consectetur<br>adipiscing elit, sed do eiusmod tempor</p></div>

    <h2 class="section-title" style="top:602px">OMELETTES</h2>
    <div class="menu-item" style="top:635px"><div class="menu-item__row"><span>Name of dish</span><span class="menu-item__leader"></span><span class="menu-item__price">$10</span></div><p class="menu-item__desc">Lorem ipsum dolor sit amet, consectetur<br>adipiscing elit, sed do eiusmod tempor</p></div>
    <div class="menu-item" style="top:686px"><div class="menu-item__row"><span>Name of dish</span><span class="menu-item__leader"></span><span class="menu-item__price">$10</span></div><p class="menu-item__desc">Lorem ipsum dolor sit amet, consectetur<br>adipiscing elit, sed do eiusmod tempor</p></div>
    <div class="menu-item" style="top:736px"><div class="menu-item__row"><span>Name of dish</span><span class="menu-item__leader"></span><span class="menu-item__price">$10</span></div><p class="menu-item__desc">Lorem ipsum dolor sit amet, consectetur<br>adipiscing elit, sed do eiusmod tempor</p></div>

    <div class="footer-band"></div>
  </section>

</main>
</body>
</html>
```